Graphic Design for LUMA KR | Frame & Drift

We are a 3D Studio in Brazil. We make 3D and 2D comercials for television, 3D ilustration for adversiting and Visual Effects for cine.
Our target is the advertising agencies.

```html
<!DOCTYPE html>
<html lang="pt-BR">
<head>
<meta charset="utf-8">
<title>LUMA KR | Frame &amp; Drift — Folder</title>
<link rel="stylesheet" href="https://fonts.googleapis.com/css2?family=IBM+Plex+Mono:wght@400;500&family=Montserrat:wght@600;700&family=Tinos&display=swap">
<style>
  :root{
    --paper:#ffffff;
    --bleed:#4fb2e3;
    --trim:#2aa0d8;
    --crop:#9a9a9a;
    --ink:#2b2b2b;
    --accent:#f08a24;
    --spine-grey:#c9c9cf;
    --paint-red:#c8321e;
    --paint-ochre:#b8995a;
    --paint-umber:#5a4028;
    --paint-sand:#d6c49a;
  }
  html,body{margin:0;padding:0;overflow:hidden;background:var(--paper);}
  .folder{display:block;width:1200px;height:832px;}
  .bleed-line{fill:none;stroke:var(--bleed);stroke-width:1;stroke-dasharray:4 3;}
  .trim-line{fill:none;stroke:var(--trim);stroke-width:1;}
  .crop-mark{stroke:var(--crop);stroke-width:.6;}
  .mark-ring{fill:none;stroke:var(--ink);stroke-width:3;}
  .mark-name{font-family:'Montserrat',sans-serif;font-weight:700;fill:var(--ink);}
  .contact-rule{stroke:var(--ink);stroke-width:1.4;}
  .contact-label{font-family:'IBM Plex Mono',monospace;font-size:7.6px;fill:var(--accent);}
  .contact-text{font-family:'IBM Plex Mono',monospace;font-size:7.6px;fill:var(--ink);}
  .spine-url{font-family:'IBM Plex Mono',monospace;font-size:9px;letter-spacing:1.5px;fill:var(--spine-grey);}
  .spine-name{font-family:'Montserrat',sans-serif;font-weight:700;font-size:11px;letter-spacing:5px;fill:var(--spine-grey);}
  .spine-accent{fill:var(--accent);}
  .brand-title{font-family:'Montserrat',sans-serif;font-weight:600;font-size:22px;letter-spacing:7px;fill:var(--ink);}
  .brand-tagline{font-family:'Tinos',serif;font-size:15px;fill:var(--ink);}
</style>
</head>
<body>
<svg class="folder" viewBox="0 0 900 624" xmlns="http://www.w3.org/2000/svg">
  <defs>
    <linearGradient id="paintingTones" x1="0" y1="0" x2="1" y2="0">
      <stop offset="0" stop-color="var(--paint-red)"/>
      <stop offset=".12" stop-color="var(--paint-umber)"/>
      <stop offset=".35" stop-color="var(--paint-ochre)"/>
      <stop offset=".55" stop-color="var(--paint-sand)"/>
      <stop offset=".75" stop-color="var(--paint-umber)"/>
      <stop offset=".9" stop-color="var(--paint-ochre)"/>
      <stop offset="1" stop-color="var(--paint-red)"/>
    </linearGradient>
    <linearGradient id="floorTones" x1="0" y1="0" x2="0" y2="1">
      <stop offset="0" stop-color="var(--paint-ochre)"/>
      <stop offset=".55" stop-color="var(--paint-umber)"/>
      <stop offset="1" stop-color="var(--paint-red)"/>
    </linearGradient>
  </defs>

  <!-- crop marks -->
  <g class="crop-marks">
    <line class="crop-mark" x1="45" y1="0" x2="45" y2="14"/>
    <line class="crop-mark" x1="0" y1="33" x2="24" y2="33"/>
    <line class="crop-mark" x1="45" y1="610" x2="45" y2="624"/>
    <line class="crop-mark" x1="0" y1="583" x2="24" y2="583"/>
    <line class="crop-mark" x1="858" y1="0" x2="858" y2="14"/>
    <line class="crop-mark" x1="878" y1="33" x2="900" y2="33"/>
    <line class="crop-mark" x1="858" y1="610" x2="858" y2="624"/>
    <line class="crop-mark" x1="878" y1="583" x2="900" y2="583"/>
  </g>

  <!-- back cover -->
  <g class="back-cover">
    <rect class="bleed-line" x="35" y="22" width="392" height="571"/>
    <rect class="trim-line" x="45" y="33" width="375" height="550"/>
    <path role="img" aria-label="Abstract expressionist painting of a crucified figure in ochre, umber and red tones"
          d="M53,42 H426 V380 Q220,388 53,425 Z" fill="url(#paintingTones)"/>

    <g class="brand-mark">
      <circle class="mark-ring" cx="101" cy="527" r="33"/>
      <text class="mark-name" x="101" y="531" font-size="11" text-anchor="middle">LUMA KR</text>
    </g>

    <line class="contact-rule" x1="150" y1="490" x2="150" y2="566"/>
    <g class="contact-block">
      <text class="contact-label" x="168" y="496">Contato.:</text>
      <text class="contact-text" x="168" y="511">+ 55 12 3415 7290</text>
      <text class="contact-text" x="168" y="522">contato@lumakr.com.br</text>
      <text class="contact-label" x="168" y="538">Local .:</text>
      <text class="contact-text" x="168" y="553">Rua Tomé Vasconcelos Arruda 418 - sala 207</text>
      <text class="contact-text" x="168" y="564">Campos do Vale - São Paulo.</text>
    </g>
  </g>

  <!-- spine -->
  <g class="spine">
    <text class="spine-url" transform="translate(453,176) rotate(-90)">www.<tspan class="spine-accent">lumakr</tspan>.com.br</text>
    <text class="spine-name" transform="translate(455,565) rotate(-90)">LUMA <tspan class="spine-accent">KR</tspan></text>
  </g>

  <!-- front cover -->
  <g class="front-cover">
    <rect class="bleed-line" x="475" y="22" width="393" height="571"/>
    <rect class="trim-line" x="475" y="33" width="383" height="550"/>
    <path role="img" aria-label="Upper part of an abstract painting of a crucified figure in ochre, umber and red tones"
          d="M475,42 H805 Q650,250 475,355 Z" fill="url(#paintingTones)"/>
    <path role="img" aria-label="Lower part of the painting: a resting hand on a red ground in ochre and umber tones"
          d="M478,575 Q560,470 690,470 Q810,472 848,545 V575 Z" fill="url(#floorTones)"/>

    <g class="brand-mark">
      <circle class="mark-ring" cx="657" cy="285" r="50"/>
      <text class="mark-name" x="657" y="291" font-size="16" text-anchor="middle">LUMA KR</text>
    </g>
    <text class="brand-title" x="604" y="363">LUMA KR</text>
    <text class="brand-tagline" x="605" y="379">Frame &amp; Drift Studio</text>
  </g>
</svg>
</body>
</html>
```